Bellwether Home Inspections

We need stationery for our new home inspection company. We inspect homes for people prior to purchasing to ensure the property is in good condition, as well as inspecting new homes to ensure they have been built to the appropriate standards. We are happy to look at combinations of colours. The use of a water mark would be good. Open to suggestions.

Industry/Entity Type

Home Inspection

```html
<!DOCTYPE html>
<html lang="en">
<head>
<meta charset="utf-8">
<title>Bellwether Home Inspections — Stationery</title>
<link rel="stylesheet" href="https://fonts.googleapis.com/css2?family=Source+Sans+3:wght@400;600;700&display=swap">
<style>
  :root {
    --backdrop: #d9d9d9;
    --paper: #ffffff;
    --brand-blue: #4470b5;
    --sky-blue: #67a7dd;
    --accent-orange: #e8a534;
    --watermark: #edf3fb;
    --ink-navy: #2e5288;
    --window-grey: #ededed;
    --window-edge: #cfcfcf;
  }
  * { margin: 0; padding: 0; box-sizing: border-box; }
  html, body { width: 1200px; height: 982px; overflow: hidden; }
  body {
    position: relative;
    background: var(--backdrop);
    font-family: "Source Sans 3", "Helvetica Neue", Arial, sans-serif;
    color: var(--paper);
  }
  .sheet { position: absolute; background: var(--paper); }

  /* Letterhead */
  .letterhead { left: 41px; top: 82px; width: 577px; height: 816px; }
  .letterhead__band { position: absolute; top: 38px; left: 0; width: 100%; height: 71px; background: var(--sky-blue); }
  .letterhead__mark { position: absolute; left: 0; top: 0; width: 147px; height: 71px; background: var(--brand-blue);
    display: flex; align-items: center; justify-content: center; gap: 6px; }
  .letterhead__contact { position: absolute; left: 432px; top: 26px; font-size: 7.5px; line-height: 9.5px; }
  .letterhead__web { position: absolute; left: 42px; top: 112px; font-size: 8px; color: var(--brand-blue); }
  .letterhead__watermark { position: absolute; left: 40px; top: 260px; width: 497px; text-align: center;
    font-size: 72px; line-height: 86px; font-weight: 600; color: var(--watermark); }
  .letterhead__footer { position: absolute; left: 0; bottom: 0; width: 100%; height: 8px; display: flex; }
  .letterhead__footer span:nth-child(1) { width: 67px; background: var(--accent-orange); }
  .letterhead__footer span:nth-child(2) { width: 123px; background: var(--brand-blue); }
  .letterhead__footer span:nth-child(3) { flex: 1; background: var(--sky-blue); }

  .wordmark { font-weight: 600; font-size: 11px; line-height: 12px; text-align: center; }
  .wordmark--light { color: var(--paper); }
  .wordmark--navy { color: var(--ink-navy); }
  .wordmark__square { width: 7px; height: 7px; background: var(--accent-orange); flex: none; }

  /* Business card front */
  .card-front { left: 663px; top: 82px; width: 242px; height: 155px; }
  .card-front__brand { position: absolute; left: 0; top: 0; width: 82px; height: 100%;
    display: flex; flex-direction: column; align-items: center; justify-content: center; gap: 5px; padding: 0 4px; }
  .card-front__rule { position: absolute; left: 82px; top: 0; width: 5px; height: 100%; background: var(--accent-orange); }
  .card-front__panel { position: absolute; left: 87px; top: 0; right: 0; height: 100%; background: var(--brand-blue); }
  .card-front__name { position: absolute; left: 14px; top: 47px; font-size: 12px; font-weight: 700; }
  .card-front__role { position: absolute; left: 14px; top: 63px; font-size: 7.5px; }
  .card-front__contact { position: absolute; left: 14px; top: 99px; font-size: 7.5px; line-height: 9.5px; }

  /* Business card back */
  .card-back { left: 668px; top: 277px; width: 240px; height: 155px; background: var(--brand-blue);
    display: flex; flex-direction: column; align-items: center; justify-content: center; gap: 10px; }
  .card-back .wordmark { font-size: 16px; line-height: 18px; }
  .card-back__web { font-size: 7.5px; }

  /* Envelope */
  .envelope { left: 660px; top: 626px; width: 497px; height: 258px; }
  .envelope__brand { position: absolute; left: 30px; top: 30px; width: 100px; display: flex; align-items: center; gap: 5px; }
  .envelope__return { position: absolute; left: 33px; top: 110px; width: 91px; height: 133px; background: var(--brand-blue); }
  .envelope__contact { position: absolute; left: 10px; bottom: 9px; font-size: 6px; line-height: 7.5px; }
  .envelope__window { position: absolute; left: 315px; top: 167px; width: 167px; height: 76px;
    background: var(--window-grey); border: 1px solid var(--window-edge); border-radius: 4px; }
</style>
</head>
<body>
  <section class="sheet letterhead" aria-label="Letterhead">
    <div class="letterhead__band">
      <div class="letterhead__mark">
        <span class="wordmark__square"></span>
        <span class="wordmark wordmark--light">Bellwether<br>Home Inspections</span>
      </div>
      <p class="letterhead__contact">482 Orchard Lane<br>Millbrook, CA 95210<br>Phone: 0555 214 380 19<br>E-mail: d.whitlock@bellwetherhome.com</p>
    </div>
    <p class="letterhead__web">bellwetherhome.com</p>
    <p class="letterhead__watermark" aria-hidden="true">Bellwether<br>Home<br>Inspections</p>
    <div class="letterhead__footer"><span></span><span></span><span></span></div>
  </section>

  <section class="sheet card-front" aria-label="Business card, front">
    <div class="card-front__brand">
      <span class="wordmark__square"></span>
      <span class="wordmark wordmark--navy">Bellwether Home Inspections</span>
    </div>
    <div class="card-front__rule"></div>
    <div class="card-front__panel">
      <p class="card-front__name">Dana Whitlock</p>
      <p class="card-front__role">manager</p>
      <p class="card-front__contact">482 Orchard Lane<br>Millbrook, CA 95210<br>Phone: 0555 214 380 19<br>E-mail: d.whitlock@bellwetherhome.com</p>
    </div>
  </section>

  <section class="sheet card-back" aria-label="Business card, back">
    <span class="wordmark__square"></span>
    <span class="wordmark wordmark--light">Bellwether<br>Home Inspections</span>
    <p class="card-back__web">bellwetherhome.com</p>
  </section>

  <section class="sheet envelope" aria-label="Envelope">
    <div class="envelope__brand">
      <span class="wordmark__square"></span>
      <span class="wordmark wordmark--navy">Bellwether<br>Home Inspections</span>
    </div>
    <div class="envelope__return">
      <p class="envelope__contact">482 Orchard Lane<br>Millbrook, CA 95210<br>Phone: 0555 214 380 19</p>
    </div>
    <div class="envelope__window"></div>
  </section>
</body>
</html>
```